Two wall artworks for physiotherapy clinic waiting room

We are a physiotherapy clinic located in Glebe, Sydney. We have a clinic that is within a beautiful heritage listed building and we have two blank white walls that need artwork. Each artwork will be 3000mm wide and 1200mm high. Our clinic is mostly white and I will include our brand's colours below. We are looking for bright, beautiful artworks that are consistent with our colours. One of the artworks should include our full logo including the text so that customers see the name of the clinic on their way into the waiting room. I will include our logo in the files below, as well as images of the clinic, the walls and some other signs that we have already. We would prefer artworks with nice patterns or graphics rather than images of people.

```html
<!DOCTYPE html>
<html lang="en">
<head>
<meta charset="utf-8">
<title>Harbour Physio – Waiting Room Wall Artwork</title>
<link rel="stylesheet" href="https://fonts.googleapis.com/css2?family=Montserrat:wght@600&family=Poppins:wght@500&display=swap">
<style>
  :root {
    --navy: #2a2570;
    --teal: #78c4bd;
    --teal-deep: #4e9c98;
    --teal-pale: #c2e5e1;
    --white: #ffffff;
    --backdrop: #eceeee;
  }
  html, body {
    margin: 0;
    width: 1200px;
    height: 900px;
    overflow: hidden;
    background: var(--backdrop);
  }
  .artwork {
    position: absolute;
    left: 0;
    top: 210px;
    width: 1200px;
    height: 480px;
    background: var(--white);
    overflow: hidden;
  }
  .graphic-zone {
    position: absolute;
  }
  .graphic-zone--left {
    left: 0;
    top: 0;
    width: 46px;
    height: 480px;
    background: linear-gradient(180deg, var(--teal-pale), var(--teal) 60%, var(--teal-deep));
  }
  .graphic-zone--top {
    left: 300px;
    top: 0;
    width: 600px;
    height: 120px;
    border-radius: 0 0 60px 60px;
    background: linear-gradient(90deg, var(--teal-pale), var(--teal) 50%, var(--teal-deep));
  }
  .graphic-zone--bottom {
    left: 0;
    top: 370px;
    width: 620px;
    height: 110px;
    border-radius: 0 60px 0 0;
    background: linear-gradient(90deg, var(--teal-deep), var(--teal) 55%, var(--teal-pale));
  }
  .graphic-zone--right {
    left: 970px;
    top: 0;
    width: 230px;
    height: 480px;
    background: linear-gradient(160deg, var(--teal-pale), var(--teal) 45%, var(--teal-deep));
  }
  .service-list {
    position: absolute;
    left: 72px;
    top: 40px;
    margin: 0;
    padding: 0;
    list-style: none;
    font-family: "Poppins", sans-serif;
    font-weight: 500;
    font-size: 19px;
    line-height: 34px;
    color: var(--navy);
    letter-spacing: -0.3px;
  }
  .brand {
    position: absolute;
    left: 190px;
    top: 180px;
    display: flex;
    align-items: center;
    gap: 22px;
  }
  .brand-dot {
    width: 70px;
    height: 70px;
    border-radius: 50%;
    background: var(--teal);
    flex: none;
  }
  .brand-name {
    font-family: "Montserrat", sans-serif;
    font-weight: 600;
    font-size: 80px;
    line-height: 1;
    color: var(--navy);
    letter-spacing: -1px;
    margin: 0;
    white-space: nowrap;
  }
  .brand-tagline {
    position: absolute;
    left: 285px;
    top: 282px;
    margin: 0;
    font-family: "Poppins", sans-serif;
    font-weight: 500;
    font-size: 25px;
    color: var(--navy);
    letter-spacing: -0.3px;
    white-space: nowrap;
  }
  .activity-icons {
    position: absolute;
    left: 780px;
    top: 380px;
    width: 140px;
    height: 76px;
    background: linear-gradient(90deg, #e6e8f2, #f2f3f8);
    border-radius: 6px;
  }
</style>
</head>
<body>
  <section class="artwork" aria-label="Wall artwork for clinic waiting room">
    <div class="graphic-zone graphic-zone--left" role="img" aria-label="Decorative teal and navy flowing band artwork"></div>
    <div class="graphic-zone graphic-zone--top" role="img" aria-label="Decorative teal and navy flowing band artwork"></div>
    <div class="graphic-zone graphic-zone--bottom" role="img" aria-label="Decorative teal and navy flowing band artwork"></div>
    <div class="graphic-zone graphic-zone--right" role="img" aria-label="Decorative teal and navy flowing band artwork"></div>

    <ul class="service-list">
      <li>Physiotherapy</li>
      <li>Exercise Physiology</li>
      <li>Classes</li>
    </ul>

    <div class="brand">
      <span class="brand-dot" aria-hidden="true"></span>
      <h1 class="brand-name">Harbour Physio</h1>
    </div>
    <p class="brand-tagline">Physiotherapy and Exercise Physiology</p>

    <div class="activity-icons" role="img" aria-label="Line icons of people lifting weights and stretching"></div>
  </section>
</body>
</html>
```